依頼詳細
★TOPラフ案について

・トップページの掲載内容はエクセルで作成した資料を添付しました。
仕様はワイヤーフレームのみですので、掲載情報が正しければ、お好きなデザインにて調整していただいて構いません。

掲載している情報のレイアウト通りではなくて大丈夫ですので
皆さまの感性にてお願いいたします。

・配置やデザイン等はアレンジしていただいて構いません。

・サイズは横幅2000pxで制作をお願いします。
縦に制限はありません。(コンテンツ幅は1100px~1200px内でお願いします。)
レスポンシブデザインのサイトで、bootstrap4を利用し、コーディングする予定になります。

・カラーイメージ
白を基調としてサブに青系、ワンポイントに赤色にてお願いします。

・ロゴ画像はヘッダーに入れる予定です。
(ロゴは青色(#00008B)で会社名ローマ字表示となります。頭文字は赤色(#FF3737)です。)

・デザインイメージ
誠実なデザインのイメージです。

デザイン選定後、決定した方には、正式な社名や連絡先を入れた修正をお願いしたいのと、
その他常識範囲で修正を依頼することもあります。
※以後、希望があれば中ページ作成及び他の案件コンテンツも継続してご依頼可能です。
ページ数
1ページ
希望イメージ
シンプル 複雑
単色 カラフル
暗い 明るい
日常 高級
遊び心 厳粛
未来的 伝統的
女性的 男性的
希望する色
青系
納品ファイル
• 高解像度JPG (.jpg)
• フォトショップ形式 (.psd)
補足説明
※ワイヤーフレーム通りのデザインでなくて、構いません。
メインビジュアル、素材などもお好みでデザインいただいて問題ございません。

仕様素材につきましてはKORVE定額素材内で使用可能な素材をご選択いただいてご使用ください。
(添付したデータ内にない素材でもご利用OKです。
その際は選定後素材№をお知らせください。)

依頼したイメージに沿ったデザインを作成いただけたためこちらのデザインに決めさせていただきました。

多くの提案をいただき本当にありがとうございました。
次回の依頼の際も是非提案いただけますようお願いいたします。

```html
<!DOCTYPE html>
<html lang="ja">
<head>
<meta charset="UTF-8">
<title>Norvale｜梱包のスペシャリスト</title>
<link href="https://fonts.googleapis.com/css2?family=Noto+Sans+JP:wght@400;500;700;900&family=Montserrat:wght@600;700;800&display=swap" rel="stylesheet">
<style>
:root{
  --navy:#00008b;
  --red:#ff3737;
  --ink:#333;
  --muted:#777;
  --line:#e2e2e2;
  --paper:#ffffff;
  --pale:#f4f5f8;
  --kraft:#c9a47a;
  --kraft-light:#e6d3b8;
}
*{margin:0;padding:0;box-sizing:border-box}
html,body{width:747px;height:1200px;overflow:hidden;background:var(--paper)}
body{font-family:"Noto Sans JP",sans-serif;color:var(--ink);font-size:7px;line-height:1.6}
.en{font-family:"Montserrat",sans-serif}

.site-header{height:35px;display:flex;align-items:center;justify-content:space-between;padding-left:24px;background:var(--paper);position:relative;z-index:2}
.brand{font-family:"Noto Sans JP",sans-serif;font-weight:700;font-size:16px;color:var(--navy);letter-spacing:.5px;line-height:1}
.header-right{display:flex;align-items:center;height:100%}
.global-nav{display:flex;gap:14px;font-size:6.5px;color:var(--ink);margin-right:14px}
.tel-button{height:100%;background:var(--navy);color:#fff;display:flex;align-items:center;gap:6px;padding:0 16px;font-weight:700;font-size:12px}
.tel-button svg{width:11px;height:11px}

.hero{position:relative;height:255px;overflow:hidden}
.hero-visual{position:absolute;inset:0;background:linear-gradient(120deg,#fbfbfc 0%,#f1ece4 38%,var(--kraft-light) 60%,var(--kraft) 82%,#b89066 100%)}
.hero-copy{position:absolute;left:28px;top:62px;font-weight:900;font-size:27px;line-height:1.45;color:var(--navy);letter-spacing:1px}

.intro{text-align:center;padding:30px 0 26px}
.intro-title{font-size:19px;font-weight:900;color:var(--navy);margin-bottom:12px}
.intro-text{font-size:6.5px;color:var(--ink);line-height:1.9}
.btn{display:inline-flex;align-items:center;justify-content:center;gap:6px;width:130px;height:20px;border-radius:10px;font-size:6.5px;font-weight:700}
.btn-red{background:var(--red);color:#fff;margin-top:12px}
.btn-outline{border:1px solid var(--line);color:var(--navy);background:#fff;width:90px;height:16px;border-radius:8px;box-shadow:0 1px 3px rgba(0,0,0,.08)}

.service{position:relative;height:175px}
.service-bg{position:absolute;left:0;right:0;top:40px;height:122px;background:var(--pale)}
.service-photo{position:absolute;left:148px;top:8px;width:225px;height:155px;background:linear-gradient(135deg,#e9e3d9 0%,#d2b48f 50%,#b8946a 100%)}
.service-body{position:absolute;left:392px;top:18px;width:220px}
.section-en{font-family:"Montserrat",sans-serif;font-weight:700;font-size:34px;line-height:1;color:#d8d8d8;letter-spacing:1px}
.section-en .initial{color:var(--red)}
.section-ja{font-size:8px;font-weight:700;color:var(--navy);margin:4px 0 10px}
.service-text{font-size:6px;line-height:1.9;color:var(--ink);margin-bottom:10px}

.photo-strip{display:flex;height:138px}
.photo-strip div{flex:1}
.strip-a{background:linear-gradient(160deg,#8a96a6,#c8ccd3 60%,#a79073)}
.strip-b{background:linear-gradient(180deg,#c9cfd8,#e9ecf0 55%,#9aa2ad)}
.strip-c{background:linear-gradient(140deg,#e9ecef,#d4d7db 55%,#c99a5e)}

.news{padding:18px 0 14px;text-align:center}
.news .section-en{font-size:26px;color:#d0d0d0}
.news .section-ja{margin:2px 0 10px}
.news-list{width:480px;margin:0 auto;text-align:left;list-style:none}
.news-item{display:flex;align-items:center;gap:10px;padding:6px 0;border-bottom:1px solid var(--line);font-size:6px}
.news-item time{color:var(--muted);width:42px}
.news-tag{background:var(--red);color:#fff;font-size:5.5px;padding:1px 6px;width:36px;text-align:center}
.news .btn-outline{margin-top:12px}

.contact{height:74px;background:var(--navy);color:#fff;display:flex;align-items:center;padding:0 70px;gap:40px}
.contact-head .en{font-size:22px;font-weight:800;line-height:1}
.contact-head p{font-size:6px;margin-top:3px}
.contact-box{text-align:center}
.contact-box .label{font-size:6px;margin-bottom:3px}
.contact-panel{background:#fff;color:var(--navy);height:32px;width:185px;display:flex;flex-direction:column;align-items:center;justify-content:center;font-weight:700}
.contact-panel .tel{font-size:14px;display:flex;align-items:center;gap:5px;line-height:1}
.contact-panel .hours{font-size:5px;color:var(--muted);font-weight:400}
.contact-mail{border:1px solid #fff;height:32px;width:185px;display:flex;align-items:center;justify-content:center;gap:6px;font-size:8px;font-weight:700}

.site-footer{text-align:center;padding-top:16px}
.site-footer .brand{font-size:18px}
.footer-nav{display:flex;justify-content:center;gap:16px;font-size:6px;margin:10px 0 10px;color:var(--ink)}
.footer-address{font-size:5.5px;color:var(--muted);line-height:1.8}
.copyright{font-size:5px;color:var(--muted);margin-top:10px}
</style>
</head>
<body>

<header class="site-header">
  <div class="brand">Norvale</div>
  <div class="header-right">
    <nav class="global-nav"><span>〇〇〇〇について</span><span>業務案内</span><span>ニュース</span><span>お問い合わせ</span></nav>
    <div class="tel-button">
      <svg viewBox="0 0 24 24" fill="#fff"><path d="M6.6 10.8a15.1 15.1 0 0 0 6.6 6.6l2.2-2.2a1 1 0 0 1 1-.25 11.4 11.4 0 0 0 3.6.57 1 1 0 0 1 1 1V20a1 1 0 0 1-1 1A17 17 0 0 1 3 4a1 1 0 0 1 1-1h3.5a1 1 0 0 1 1 1c0 1.25.2 2.45.57 3.57a1 1 0 0 1-.25 1z"/></svg>
      <span class="en">00-0000-0000</span>
    </div>
  </div>
</header>

<section class="hero">
  <div class="hero-visual" role="img" aria-label="段ボール箱が積み重なった梱包のイメージ写真"></div>
  <h1 class="hero-copy">梱包が変わると、<br>流通が変わる。</h1>
</section>

<section class="intro">
  <h2 class="intro-title">〇〇〇〇は梱包のスペシャリストです。</h2>
  <p class="intro-text">私たちは〇〇〇〇を通じて、お客様の大切な商品を安全にお届けします。<br>確かな技術と丁寧な仕事で、物流を支えます。<br>豊富な実績をもとに最適な梱包をご提案します。</p>
  <a class="btn btn-red">詳しくはこちら ›</a>
</section>

<section class="service">
  <div class="service-bg"></div>
  <div class="service-photo" role="img" aria-label="作業員が段ボール箱を梱包している写真"></div>
  <div class="service-body">
    <p class="section-en"><span class="initial">P</span>acking</p>
    <h3 class="section-ja">業務案内</h3>
    <p class="service-text">梱包材の選定から作業まで一貫対応。<br>精密機器や大型製品など幅広い商品に対応し、<br>コストと品質の両立を実現します。<br>お気軽にご相談ください。</p>
    <a class="btn btn-outline">詳しくはこちら ›</a>
  </div>
</section>

<div class="photo-strip">
  <div class="strip-a" role="img" aria-label="倉庫に並ぶ荷物の写真"></div>
  <div class="strip-b" role="img" aria-label="物流倉庫の通路の写真"></div>
  <div class="strip-c" role="img" aria-label="テープで箱を封する手元の写真"></div>
</div>

<section class="news">
  <p class="section-en"><span class="initial">N</span>ews</p>
  <h3 class="section-ja">ニュース</h3>
  <ul class="news-list">
    <li class="news-item"><time>2024.00.00</time><span class="news-tag">お知らせ</span><span>年末年始の営業日についてのご案内を掲載しました。</span></li>
    <li class="news-item"><time>2024.00.00</time><span class="news-tag">お知らせ</span><span>新しい梱包サービスの提供を開始いたしました。</span></li>
    <li class="news-item"><time>2024.00.00</time><span class="news-tag">お知らせ</span><span>ホームページをリニューアルいたしました。</span></li>
  </ul>
  <a class="btn btn-outline">一覧へ ›</a>
</section>

<section class="contact">
  <div class="contact-head">
    <p class="en">Contact</p>
    <p>お問い合わせ</p>
  </div>
  <div class="contact-box">
    <p class="label">お電話でのお問い合わせ</p>
    <div class="contact-panel">
      <span class="tel en"><svg width="11" height="11" viewBox="0 0 24 24" fill="#00008b"><path d="M6.6 10.8a15.1 15.1 0 0 0 6.6 6.6l2.2-2.2a1 1 0 0 1 1-.25 11.4 11.4 0 0 0 3.6.57 1 1 0 0 1 1 1V20a1 1 0 0 1-1 1A17 17 0 0 1 3 4a1 1 0 0 1 1-1h3.5a1 1 0 0 1 1 1c0 1.25.2 2.45.57 3.57a1 1 0 0 1-.25 1z"/></svg>00-0000-0000</span>
      <span class="hours">受付 9:00〜18:00（土日祝除く）</span>
    </div>
  </div>
  <div class="contact-box">
    <p class="label">メールでのお問い合わせ</p>
    <div class="contact-mail">
      <svg width="12" height="9" viewBox="0 0 24 18" fill="none" stroke="#fff" stroke-width="2"><rect x="1" y="1" width="22" height="16"/><path d="M1 1l11 9 11-9"/></svg>
      メールフォームへ
    </div>
  </div>
</section>

<footer class="site-footer">
  <div class="brand">Norvale</div>
  <nav class="footer-nav"><span>ホーム</span><span>〇〇〇〇について</span><span>業務案内</span><span>ニュース</span><span>お問い合わせ</span><span>プライバシーポリシー</span></nav>
  <p class="footer-address">株式会社〇〇〇〇<br>〒000-0000 〇〇県〇〇市〇〇町0-0-0<br>TEL 00-0000-0000 / FAX 00-0000-0000</p>
  <p class="copyright">© Norvale All Rights Reserved.</p>
</footer>

</body>
</html>
```